New Dental Office Needs an Attractive and user friendly Website Designed

I need a website for a new dental office. The Name is Maplecrest Dentistry. I would like a Modern design with a user friendly interface and usability.
I would like a landing page, a page that lists the services we offer: Cosmetic Dentistry, Implants, Dental Hygiene, Emergency Services, Restorations, Dentures
Target Market(s)
Mid to upper class
Industry/Entity Type
Dentistry
Coding
Coded - Design and coding required
Number of Pages Required
1 page
Requirements
Must have
- Landing page that has a scheduling option, Procedures, operating hours, and contact us info
Nice to have
- Appealing design, Soft comforting colors. Easy to navigate page, Modern and professional.

```html
<!DOCTYPE html>
<html lang="en">
<head>
<meta charset="utf-8">
<title>Maplecrest Dentistry</title>
<link href="https://fonts.googleapis.com/css2?family=Inter:wght@400;500;600;700&display=swap" rel="stylesheet">
<style>
:root{
  --blue:#0c5fb0;
  --blue-dark:#0a4f96;
  --red:#e3262a;
  --ink:#111418;
  --text:#5a5f66;
  --navy:#0b1b33;
  --line:#d5dbe3;
  --card-teal:#dce9ee;
  --card-lilac:#e2e4f4;
  --card-rose:#f1e4e1;
}
*{box-sizing:border-box;margin:0;padding:0}
html,body{width:1200px;height:3053px;overflow:hidden}
body{font-family:"Inter",Arial,sans-serif;color:var(--ink);background:#fff;position:relative}
.abs{position:absolute}
a{color:inherit;text-decoration:none}
.eyebrow{font-size:12px;font-weight:600;letter-spacing:2.6px;color:var(--red);display:flex;align-items:center;gap:10px;text-transform:uppercase}
.eyebrow::before{content:"";width:26px;height:2px;background:var(--red)}
.heading{font-weight:700;color:var(--ink);letter-spacing:-.5px;line-height:1.12}
.heading .accent{color:var(--blue)}
.body-copy{font-size:11px;line-height:1.52;color:var(--text)}
.btn{display:inline-flex;align-items:center;justify-content:center;font-size:10px;font-weight:700;text-transform:uppercase;height:36px;padding:0 15px;white-space:nowrap}
.btn-solid{background:var(--blue);color:#fff}
.btn-outline{border:1px solid var(--blue);color:var(--blue);background:#fff}
.photo{position:absolute}

/* top bar */
.topbar{top:0;left:0;width:1200px;height:30px;background:var(--blue);color:#fff;font-size:11px;font-weight:500}
.topbar .group{position:absolute;top:8px;left:210px;display:flex;gap:16px}
.topbar .item{display:flex;align-items:center;gap:6px;white-space:nowrap}

/* header */
.logo{font-weight:700;color:var(--blue);font-size:22px;letter-spacing:-.3px;line-height:1.05}
.logo small{display:block;font-size:11px;letter-spacing:4px;font-weight:700}
.nav{top:57px;right:330px;display:flex;gap:20px;font-size:11px;color:#333;white-space:nowrap}
.nav .active{color:var(--red)}

/* hero */
.hero-bg{top:97px;left:0;width:777px;height:459px;background:linear-gradient(90deg,#e7eef3 0%,#f6f9fb 40%,#fff 70%)}
.info{display:flex;gap:10px;align-items:flex-start}
.info .label{font-size:11px;color:#555;text-transform:uppercase}
.info .value{font-size:11px;color:var(--blue);font-weight:600;margin-top:2px}

/* progress */
.bar-row{position:absolute;left:600px;width:391px}
.bar-row .name{font-size:13px;font-weight:600;color:var(--blue)}
.bar-row .track{position:absolute;left:0;top:23px;width:391px;height:6px;background:#c7dae9;border-radius:3px}
.bar-row .fill{height:6px;background:var(--blue);border-radius:3px}
.bar-row .pct{position:absolute;top:0;background:var(--red);color:#fff;font-size:10px;font-weight:700;padding:2px 4px;border-radius:2px}

/* services */
.svc-card{position:absolute;top:1252px;width:194px;height:196px;padding:0 23px}
.svc-card h3{position:absolute;left:23px;bottom:30px;font-size:19px;font-weight:600;line-height:1.2;color:var(--ink)}
.svc-card svg{position:absolute;left:22px;top:45px}
.arrow{position:absolute;top:1342px}

/* why choose */
.feature{position:absolute;left:210px;width:400px;height:60px}
.feature .icon{position:absolute;left:0;top:0;width:50px;height:50px;background:#eeeeef;display:flex;align-items:center;justify-content:center}
.feature h4{position:absolute;left:67px;top:0;font-size:14px;font-weight:600;color:var(--blue)}
.feature p{position:absolute;left:67px;top:21px;font-size:10.5px;line-height:1.45;color:var(--text);width:340px}

/* news */
.news-card{position:absolute;top:2514px;width:257px;padding:25px 26px}
.news-card .date{font-size:11px;color:#777}
.news-card h4{font-size:15px;font-weight:600;color:var(--blue);line-height:1.3;margin-top:12px}
.news-card p{font-size:10.5px;line-height:1.42;color:var(--text);margin-top:10px}
.news-card .more{display:block;font-size:10px;color:var(--red);font-weight:600;margin-top:8px;text-transform:uppercase}

/* footer */
.footer{top:2750px;left:0;width:1200px;height:303px;background:var(--navy);color:#fff}
.footer h5{font-size:13px;font-weight:600;text-transform:uppercase;margin-bottom:14px}
.footer ul{list-style:none;font-size:11px;color:#c9d1dc;line-height:20px}
.footer .col{position:absolute;top:76px}
.contact li{display:flex;align-items:center;gap:9px}
.social{display:flex;gap:24px}
.social span{width:14px;height:14px;border-radius:50%;background:#fff;display:block}
</style>
</head>
<body>

<!-- Top bar -->
<div class="abs topbar">
  <div class="group">
    <div class="item">
      <svg width="11" height="11" viewBox="0 0 24 24" fill="#fff"><path d="M6.6 10.8a15 15 0 0 0 6.6 6.6l2.2-2.2c.3-.3.7-.4 1-.2 1.1.4 2.3.6 3.6.6.6 0 1 .4 1 1V20c0 .6-.4 1-1 1A17 17 0 0 1 3 4c0-.6.4-1 1-1h3.5c.6 0 1 .4 1 1 0 1.3.2 2.5.6 3.6.1.3 0 .7-.2 1z"/></svg>
      +1 (555) 014 2270
    </div>
    <div class="item">
      <svg width="12" height="10" viewBox="0 0 24 18" fill="none" stroke="#fff" stroke-width="2"><rect x="1" y="1" width="22" height="16"/><path d="M1 1l11 9 11-9"/></svg>
      hello@maplecrestdental.com
    </div>
  </div>
  <div class="item" style="position:absolute;top:8px;right:210px">
    <svg width="12" height="12" viewBox="0 0 24 24" fill="none" stroke="#fff" stroke-width="2"><circle cx="12" cy="12" r="10"/><path d="M12 6v6l4 2"/></svg>
    Monday to Friday 8:00 - 6:30
  </div>
</div>

<!-- Header -->
<div class="abs logo" style="top:44px;left:210px">Maplecrest<small>DENTISTRY</small></div>
<nav class="abs nav">
  <a class="active">Home</a><a>About Us</a><a>Services</a><a>Why Choose Us</a><a>Blog</a><a>Contact</a>
</nav>
<a class="abs btn btn-solid" style="top:45px;left:896px;width:94px;height:37px;padding:0">Appoint Now</a>

<!-- Hero -->
<div class="abs hero-bg"></div>
<div class="photo" role="img" aria-label="Bright modern dental treatment room" style="top:97px;left:777px;width:423px;height:459px;background:linear-gradient(160deg,#eef3f8,#c9d6e3 60%,#aebdcd)"></div>
<div class="photo" role="img" aria-label="Dentist examining a smiling patient" style="top:160px;left:645px;width:266px;height:330px;border-radius:133px 133px 0 0;background:linear-gradient(160deg,#2d6fb0,#9db7c9 55%,#d8c3b3)"></div>
<div class="abs" style="top:174px;left:675px;width:9px;height:9px;background:var(--blue)"></div>
<div class="abs" style="top:508px;left:760px;width:12px;height:12px;background:var(--blue)"></div>
<div class="abs" style="top:482px;left:625px;width:6px;height:6px;background:var(--blue)"></div>

<div class="abs eyebrow" style="top:180px;left:210px">Work With Us</div>
<h1 class="abs heading" style="top:204px;left:209px;font-size:39px">Become Reason of<br><span class="accent">Thousand Smiles</span></h1>
<p class="abs body-copy" style="top:302px;left:210px;width:375px">Lorem ipsum dolor sit amet, consectetur adipiscing elit, sed do eiusmod tempor incididunt ut labore et dolore magna aliqua. Ut enim ad minim veniam, quis nostrud exercitation ullamco laboris nisi ut aliquip ex ea commodo consequat.</p>
<a class="abs btn btn-solid" style="top:387px;left:210px;width:95px;padding:0">Appoint Now</a>
<a class="abs btn btn-outline" style="top:387px;left:314px;width:95px;padding:0">Contact Us</a>
<div class="abs info" style="top:450px;left:210px">
  <svg width="22" height="26" viewBox="0 0 24 28" fill="none" stroke="#e3262a" stroke-width="1.8"><path d="M12 26s-9-9-9-15a9 9 0 0 1 18 0c0 6-9 15-9 15z"/><circle cx="12" cy="11" r="3.2"/></svg>
  <div><div class="label">Address</div><div class="value">Lorenipsumdolor Street, 87</div></div>
</div>
<div class="abs info" style="top:450px;left:409px">
  <svg width="24" height="24" viewBox="0 0 24 24" fill="none" stroke="#e3262a" stroke-width="1.8"><circle cx="12" cy="12" r="10.5"/><path d="M12 6v6l4 3"/></svg>
  <div><div class="label">Opening Hours</div><div class="value">Mon-Fri 8:00 - 16:00</div></div>
</div>

<!-- About -->
<div class="photo" role="img" aria-label="Glass-walled clinic interior" style="top:684px;left:0;width:525px;height:351px;background:linear-gradient(110deg,#dfe4ea,#f4f6f8 50%,#cfd6de)"></div>
<div class="abs" style="top:700px;left:270px;width:256px;height:335px;border-radius:128px 128px 0 0;background:var(--blue)"></div>
<div class="photo" role="img" aria-label="Smiling dentist in white uniform holding a dental model" style="top:617px;left:240px;width:340px;height:418px;background:radial-gradient(ellipse at 50% 70%,#f3f3f3 0%,#e6e8eb 45%,rgba(230,232,235,0) 70%)"></div>

<div class="abs eyebrow" style="top:630px;left:600px">About Maplecrest</div>
<h2 class="abs heading" style="top:652px;left:599px;font-size:32px">Best Dental Clinic That<br><span class="accent">You Can Trust</span></h2>
<p class="abs body-copy" style="top:732px;left:600px;width:375px">Lorem ipsum dolor sit amet consectetur adipiscing elit, sed do eiusmod tempor incididunt ut labore et dolore magna aliqua. Ut enim ad minim veniam, quis nostrud exercitation ullamco laboris nisi ut aliquip ex ea commodo consequat.</p>

<div class="bar-row" style="top:822px"><span class="name">Enddodentic Equipments</span><span class="pct" style="left:342px">98%</span><div class="track"><div class="fill" style="width:373px"></div></div></div>
<div class="bar-row" style="top:862px"><span class="name">Dental Operatory Lights</span><span class="pct" style="left:331px">95%</span><div class="track"><div class="fill" style="width:361px"></div></div></div>
<div class="bar-row" style="top:902px"><span class="name">Operatory Cabinetory</span><span class="pct" style="left:331px">95%</span><div class="track"><div class="fill" style="width:361px"></div></div></div>
<div class="bar-row" style="top:942px"><span class="name">Surgical Microscope</span><span class="pct" style="left:342px">96%</span><div class="track"><div class="fill" style="width:373px"></div></div></div>
<a class="abs btn btn-outline" style="top:996px;left:602px;height:37px;width:95px;padding:0">Learn More</a>

<!-- Services -->
<div class="abs eyebrow" style="top:1120px;left:210px">Services</div>
<h2 class="abs heading" style="top:1142px;left:209px;font-size:30px">Comprehensive Service<br>For <span class="accent">Our Patients</span></h2>
<div class="abs" style="top:1146px;left:572px;width:1px;height:62px;background:var(--line)"></div>
<p class="abs body-copy" style="top:1144px;left:600px;width:375px">Lorem ipsum dolor sit amet consectetur adipiscing elit, sed do eiusmod tempor incididunt ut labore et dolore magna aliqua. Ut enim ad minim veniam, quis nostrud exercitation ullamco laboris nisi ut aliquip ex ea commodo consequat.</p>

<svg class="arrow" style="left:178px" width="12" height="16" viewBox="0 0 12 16" fill="none" stroke="#0c5fb0" stroke-width="2"><path d="M9 2L3 8l6 6"/></svg>
<svg class="arrow" style="left:1012px" width="12" height="16" viewBox="0 0 12 16" fill="none" stroke="#0c5fb0" stroke-width="2"><path d="M3 2l6 6-6 6"/></svg>

<div class="svc-card" style="left:210px;background:var(--card-teal)">
  <svg width="52" height="56" viewBox="0 0 52 56" fill="none" stroke="#e3262a" stroke-width="2"><path d="M18 22c-6-3-12 1-11 9 1 6 3 9 4 16 1 5 5 5 6 0l2-7c1-3 4-3 5 0l2 7c1 5 5 5 6 0 1-7 3-10 4-16 1-8-5-12-11-9-2 1-5 1-7 0z"/><path d="M4 12l14-6M8 5l4 8"/></svg>
  <h3>Cosmetic<br>Dentistry</h3>
</div>
<div class="photo" role="img" aria-label="Dentist reviewing a dental X-ray on a tablet" style="top:1252px;left:405px;width:194px;height:411px;background:linear-gradient(180deg,#d9dcdf,#9ea4aa 55%,#2b2e31)"></div>
<div class="abs" style="top:1620px;left:425px;font-size:19px;font-weight:600;color:#fff">Implants</div>
<div class="svc-card" style="left:600px;background:var(--card-lilac)">
  <svg width="70" height="62" viewBox="0 0 70 62" fill="none" stroke="#e3262a" stroke-width="2"><path d="M4 56L36 18M30 12l14 12M34 8l4-4M40 14l4-4M46 20l4-4"/><path d="M48 32c-4-2-9 1-8 6 1 4 2 6 3 11 1 3 3 3 4 0l1-4h2l1 4c1 3 3 3 4 0 1-5 2-7 3-11 1-5-4-8-8-6z"/><path d="M62 4v8M58 8h8"/></svg>
  <h3>Dental<br>Hygiene</h3>
</div>
<div class="svc-card" style="left:795px;background:var(--card-rose)">
  <svg width="64" height="62" viewBox="0 0 64 62" fill="none" stroke="#e3262a" stroke-width="2"><path d="M8 10c-4 4-4 14 8 28s24 18 28 14l4-4-8-8-5 4c-4-2-12-10-14-14l4-5-8-8z"/><circle cx="46" cy="16" r="12"/><path d="M46 10v12M40 16h12"/><circle cx="14" cy="48" r="8"/><path d="M14 44v5M14 52v.5"/></svg>
  <h3>Emergency<br>Services</h3>
</div>
<p class="abs body-copy" style="top:1480px;left:626px;width:368px">Sed ut perspiciatis unde omnis iste natus error sit voluptatem accusantium doloremque laudantium, totam rem aperiam, eaque ipsa quae ab illo inventore veritatis et quasi architecto beatae vitae dicta sunt explicabo. Nemo enim ipsam voluptatem quia voluptas sit aspernatur aut odit aut fugit, sed quia consequuntur magni dolores eos qui ratione voluptatem sequi nesciunt.</p>
<a class="abs btn btn-solid" style="top:1599px;left:627px;height:36px;width:95px;padding:0">Learn More</a>

<!-- Why choose us -->
<div class="photo" role="img" aria-label="Dentist treating a relaxed patient in a dental chair" style="top:1757px;left:610px;width:590px;height:520px;background:linear-gradient(90deg,#fff 0%,#eef2f6 25%,#d8e0e8 60%,#c4d1dc)"></div>
<div class="abs eyebrow" style="top:1756px;left:210px">Why Choose Us</div>
<h2 class="abs heading" style="top:1778px;left:209px;font-size:32px">A Leading Visionary In<br><span class="accent">Dental Care</span></h2>
<p class="abs body-copy" style="top:1862px;left:210px;width:400px">Lorem ipsum dolor sit amet consectetur adipiscing elit, sed do eiusmod tempor incididunt ut labore et dolore magna aliqua. Ut enim ad minim veniam, quis nostrud exercitation ullamco laboris nisi ut aliquip.</p>

<div class="feature" style="top:1933px">
  <div class="icon"><svg width="30" height="28" viewBox="0 0 30 28" fill="none" stroke="#e3262a" stroke-width="1.6"><path d="M10 6c-5-2-9 1-8 7 1 4 2 6 3 11 1 3 3 3 4 0l1-4h2l1 4c1 3 3 3 4 0 1-5 2-7 3-11 1-6-3-9-8-7z"/><path d="M22 3l5 5M24 10l4-2"/></svg></div>
  <h4>Quality Services</h4><p>Lorem ipsum dolor sit amet consectetur adipiscing elit, sed do eius mod tempor incididunt ut labore et dolore magna aliqua.</p>
</div>
<div class="feature" style="top:2004px">
  <div class="icon"><svg width="28" height="30" viewBox="0 0 28 30" fill="none" stroke="#e3262a" stroke-width="1.6"><rect x="3" y="3" width="14" height="24"/><rect x="6" y="7" width="8" height="6"/><path d="M17 12h5v12h-5M7 18c0 3 2 5 3 5s3-2 3-5"/></svg></div>
  <h4>Modern Technology</h4><p>Lorem ipsum dolor sit amet consectetur adipiscing elit, sed do eius mod tempor incididunt ut labore et dolore magna aliqua.</p>
</div>
<div class="feature" style="top:2075px">
  <div class="icon"><svg width="26" height="30" viewBox="0 0 26 30" fill="none" stroke="#e3262a" stroke-width="1.6"><circle cx="13" cy="8" r="5"/><path d="M3 28c0-7 4-11 10-11s10 4 10 11zM9 18l4 5 4-5M13 23v5"/></svg></div>
  <h4>Professional Doctor</h4><p>Lorem ipsum dolor sit amet consectetur adipiscing elit, sed do eius mod tempor incididunt ut labore et dolore magna aliqua.</p>
</div>
<a class="abs btn btn-outline" style="top:2149px;left:210px;height:36px;width:95px;padding:0">Learn More</a>

<div class="abs" style="top:1939px;left:661px;width:154px;height:182px;background:var(--blue);color:#fff;text-align:center">
  <div style="margin:21px auto 0;width:82px;height:82px;border-radius:50%;background:#fff;display:flex;align-items:center;justify-content:center;color:var(--blue);font-size:10px;font-weight:700;line-height:1.1">Maplecrest<br>Dentistry</div>
  <div style="font-size:10px;font-weight:500;margin-top:20px">HAVE ANY QUESTION</div>
  <div style="font-size:15px;font-weight:500;margin-top:7px;letter-spacing:-.3px;white-space:nowrap">+1 (555) 014 2270</div>
</div>

<!-- News -->
<div class="abs" style="top:2277px;left:0;width:542px;height:68px;background:var(--blue)"></div>
<div class="abs" style="top:2345px;left:0;width:476px;height:405px;background:linear-gradient(180deg,var(--blue) 0%,#1474c8 100%)"></div>
<div class="photo" role="img" aria-label="Doctor in white coat with a stethoscope and blue gloves" style="top:2277px;left:0;width:245px;height:473px;background:linear-gradient(100deg,#eef1f4 0%,#c9d6e2 55%,rgba(12,95,176,0) 100%)"></div>
<div class="abs" style="top:2512px;left:245px;width:231px;height:1px;background:rgba(255,255,255,.25)"></div>
<h2 class="abs" style="top:2344px;left:275px;font-size:26px;font-weight:600;color:#fff;line-height:1.13;letter-spacing:-.4px">Last News<br>From Our<br>Dental Office</h2>
<a class="abs btn" style="top:2449px;left:276px;height:37px;width:95px;padding:0;border:1px solid #fff;color:#fff">More News</a>
<div class="abs" style="top:2578px;left:275px;font-size:17px;font-weight:600;color:#fff">Let's Be A Part Of Us</div>
<div class="abs" style="top:2613px;left:276px;width:173px;height:40px;display:flex">
  <div style="flex:1;background:#fff;font-size:9px;color:#777;display:flex;align-items:center;padding-left:10px">Enter your email</div>
  <div style="width:52px;background:#1b96e3;color:#fff;font-size:10px;font-weight:700;display:flex;align-items:center;justify-content:center">SEND</div>
</div>

<div class="photo" role="img" aria-label="Dentist treating a patient lying in a chair" style="top:2345px;left:476px;width:257px;height:169px;background:linear-gradient(160deg,#e4e9ee,#9fb2c4 60%,#3a5f8c)"></div>
<div class="photo" role="img" aria-label="Dentist with face shield treating a smiling patient" style="top:2345px;left:733px;width:257px;height:169px;background:linear-gradient(160deg,#eef1f3,#b9c5d0 60%,#5c6f85)"></div>
<div class="news-card" style="left:476px">
  <div class="date">19th May, 2025</div>
  <h4>Excepteur sint occaecat cupid atat non proident</h4>
  <p>Lorem ipsum dolor sit amet consectetur adipiscing elit, sed do eiusmod tempor incididunt ut labore et dolore magna aliqua. Ut enim ad minim veniam.</p>
  <a class="more">Learn More</a>
</div>
<div class="news-card" style="left:737px">
  <div class="date">19th May, 2025</div>
  <h4>Excepteur sint occaecat cupid atat non proident</h4>
  <p>Lorem ipsum dolor sit amet consectetur adipiscing elit, sed do eiusmod tempor incididunt ut labore et dolore magna aliqua.</p>
  <a class="more">Learn More</a>
</div>

<!-- Footer -->
<footer class="abs footer">
  <div class="abs logo" style="top:72px;left:210px;color:#fff;font-size:24px">Maplecrest<small>DENTISTRY</small></div>
  <div class="abs" style="top:164px;left:210px">
    <h5 style="font-size:12px">Follow Us On</h5>
    <div class="social"><span></span><span></span><span></span></div>
  </div>
  <div class="col" style="left:428px"><h5>Quick Link</h5><ul><li>Home</li><li>About Us</li><li>Services</li><li>Why Choose Us</li><li>Blog</li><li>Contact</li></ul></div>
  <div class="col" style="left:588px"><h5>Services</h5><ul><li>Cosmetic Dentistry</li><li>Implants</li><li>Dental Hygiene</li><li>Emergency Services</li><li>Restorations</li><li>Dentures</li></ul></div>
  <div class="col contact" style="left:774px"><h5>Contact</h5><ul>
    <li><svg width="11" height="12" viewBox="0 0 24 28" fill="none" stroke="#fff" stroke-width="2.4"><path d="M12 26s-9-9-9-15a9 9 0 0 1 18 0c0 6-9 15-9 15z"/><circle cx="12" cy="11" r="3"/></svg>Lorenipsumdolor Street, 87</li>
    <li><svg width="11" height="11" viewBox="0 0 24 24" fill="#fff"><path d="M6.6 10.8a15 15 0 0 0 6.6 6.6l2.2-2.2c.3-.3.7-.4 1-.2 1.1.4 2.3.6 3.6.6.6 0 1 .4 1 1V20c0 .6-.4 1-1 1A17 17 0 0 1 3 4c0-.6.4-1 1-1h3.5c.6 0 1 .4 1 1 0 1.3.2 2.5.6 3.6.1.3 0 .7-.2 1z"/></svg>+1 (555) 014 2270</li>
    <li><svg width="11" height="9" viewBox="0 0 24 18" fill="none" stroke="#fff" stroke-width="2.4"><rect x="1" y="1" width="22" height="16"/><path d="M1 1l11 9 11-9"/></svg>hello@maplecrestdental.com</li>
    <li><svg width="11" height="11" viewBox="0 0 24 24" fill="none" stroke="#fff" stroke-width="2.4"><circle cx="12" cy="12" r="10"/><path d="M12 6v6l4 2"/></svg>Monday to Friday 8:00 - 6:30</li>
  </ul></div>
  <div class="abs" style="top:250px;left:210px;width:780px;height:1px;background:rgba(255,255,255,.18)"></div>
  <div class="abs" style="top:268px;left:210px;font-size:11px;color:#c9d1dc">Copyright © 2025 maplecrestdental.com. All Rights Reserved. &nbsp;|&nbsp; Privacy Policy</div>
</footer>

</body>
</html>
```